Postcard Design

Northgate Tidy Works Company Inc, is a air duct cleaning, dryer vent cleaning & pressure washing company, we would like this postcard to focus fully on our pressure washing specials for the season.

Industry/Entity Type

It Company

```html
<!DOCTYPE html>
<html lang="en">
<head>
<meta charset="utf-8">
<title>Pressure Washing Specials Postcard</title>
<link rel="stylesheet" href="https://fonts.googleapis.com/css2?family=Rye&family=Arvo:wght@400;700&family=Yellowtail&family=Oswald:wght@500&display=block">
<style>
  :root {
    --backdrop: #e9e6e1;
    --teal: #55b8ba;
    --teal-deep: #2f8f93;
    --red: #c81e32;
    --ink: #1d2a2c;
    --yellow: #f6d233;
    --white: #ffffff;
  }
  html, body {
    margin: 0;
    width: 1200px;
    height: 900px;
    overflow: hidden;
    background: var(--backdrop);
  }
  .postcard {
    position: absolute;
    left: 45px;
    top: 20px;
    width: 840px;
    height: 650px;
    transform: scale(1.3214);
    transform-origin: 0 0;
    background: var(--teal);
    overflow: hidden;
    box-shadow: 0 2px 10px rgba(0,0,0,.25);
  }
  .postcard-shapes { position: absolute; inset: 0; }
  .headline {
    position: absolute;
    left: 367px;
    width: 460px;
    text-align: center;
    font-family: "Rye", serif;
    font-weight: 400;
    color: var(--red);
    text-shadow: 2px 2px 0 var(--white);
    margin: 0;
    line-height: 1;
    white-space: nowrap;
    transform-origin: 50% 0;
  }
  .headline-main { top: 40px; font-size: 120px; transform: scaleX(0.56); }
  .headline-top { top: 36px; font-size: 36px; transform: scaleX(0.78); z-index: 1; }
  .divider {
    position: absolute;
    left: 395px;
    width: 410px;
    border-top: 2px dotted #234a4c;
  }
  .divider-top { top: 184px; }
  .divider-bottom { top: 358px; }
  .intro {
    position: absolute;
    left: 382px;
    width: 432px;
    top: 194px;
    margin: 0;
    text-align: center;
    font-family: "Arvo", serif;
    font-size: 15px;
    line-height: 22.5px;
    color: var(--ink);
  }
  .services {
    position: absolute;
    top: 268px;
    margin: 0;
    padding: 0;
    list-style: none;
    font-family: "Arvo", serif;
    font-size: 15px;
    line-height: 23px;
    color: var(--ink);
  }
  .services-left { left: 389px; }
  .services-right { left: 574px; }
  .services li { position: relative; padding-left: 24px; white-space: nowrap; }
  .services li::before {
    content: "";
    position: absolute;
    left: 0;
    top: 4px;
    width: 15px;
    height: 15px;
    border-radius: 50%;
    background: var(--yellow);
  }
  .call-line {
    position: absolute;
    left: 380px;
    width: 440px;
    top: 383px;
    margin: 0;
    text-align: center;
    font-family: "Yellowtail", "Brush Script MT", cursive;
    font-size: 46px;
    line-height: 52px;
    color: var(--red);
    text-shadow: 1px 1px 0 var(--white);
  }
  .call-number {
    position: absolute;
    left: 380px;
    width: 440px;
    top: 434px;
    margin: 0;
    text-align: center;
    font-family: "Oswald", sans-serif;
    font-weight: 500;
    font-size: 40px;
    line-height: 48px;
    color: var(--red);
    transform: skewX(-10deg);
  }
  .brand-name {
    position: absolute;
    left: 390px;
    top: 532px;
    margin: 0;
    white-space: nowrap;
    font-family: "Arvo", serif;
    font-weight: 700;
    font-size: 22px;
    line-height: 28px;
    color: var(--white);
  }
  .web-address {
    position: absolute;
    left: 380px;
    width: 440px;
    top: 608px;
    margin: 0;
    text-align: center;
    font-family: "Arvo", serif;
    font-size: 13px;
    letter-spacing: 3px;
    color: var(--ink);
  }
  .offer-stamp {
    position: absolute;
    left: 215px;
    top: 472px;
    width: 144px;
    height: 144px;
    border-radius: 50%;
    background: var(--white);
    display: flex;
    align-items: center;
    justify-content: center;
  }
  .offer-stamp-ring {
    width: 120px;
    height: 120px;
    border-radius: 50%;
    border: 10px solid var(--red);
    box-sizing: border-box;
    display: flex;
    flex-direction: column;
    align-items: center;
    justify-content: center;
    transform: rotate(-14deg);
    font-family: "Arvo", serif;
    font-weight: 700;
    color: var(--red);
    line-height: 1;
  }
  .offer-percent { font-size: 34px; }
  .offer-off { font-size: 20px; letter-spacing: 1px; }
</style>
</head>
<body>
<main class="postcard">
  <svg class="postcard-shapes" viewBox="0 0 840 650" width="840" height="650">
    <defs>
      <linearGradient id="photoTone" x1="0" y1="0" x2="0.6" y2="1">
        <stop offset="0" stop-color="#b9bcbf"/>
        <stop offset="0.5" stop-color="#6f7c8c"/>
        <stop offset="1" stop-color="#7e7456"/>
      </linearGradient>
    </defs>
    <path class="accent-band" d="M150,0 L250,0 C430,150 420,470 230,650 L175,650 Z" fill="var(--teal-deep)"/>
    <path class="photo-area" role="img" aria-label="Photo of a worker in yellow boots pressure washing a concrete floor"
          d="M0,0 L150,0 C330,110 400,420 175,650 L0,650 Z" fill="url(#photoTone)"/>
    <path class="photo-frame" d="M150,0 C330,110 400,420 175,650" fill="none" stroke="var(--white)" stroke-width="12"/>
    <circle class="member-badge" cx="739" cy="545" r="40" fill="none" stroke="#33575a" stroke-width="3"/>
  </svg>

  <h2 class="headline headline-main">SPECIALS</h2>
  <h1 class="headline headline-top">PRESSURE WASHING</h1>

  <div class="divider divider-top"></div>
  <p class="intro">With a 4500 PSI heated truck-mounted<br>pressure washer, we can make any project look<br>brand new.&nbsp; We have experience in:</p>
  <ul class="services services-left">
    <li>Fleet Washes</li>
    <li>Whole Homes</li>
    <li>Apartments</li>
  </ul>
  <ul class="services services-right">
    <li>Drive Thrus</li>
    <li>Commercial Building</li>
    <li>Sidewalks &amp; Much More!</li>
  </ul>
  <div class="divider divider-bottom"></div>

  <p class="call-line">Call Us Today At</p>
  <p class="call-number">(555) 014-2287</p>

  <p class="brand-name">Northgate Tidy Works</p>
  <p class="web-address">www.northgatetidyworks.com</p>

  <div class="offer-stamp">
    <div class="offer-stamp-ring">
      <span class="offer-percent">50%</span>
      <span class="offer-off">OFF</span>
    </div>
  </div>
</main>
</body>
</html>
```